PTA Meeting Poster

We are looking to create a poster to invite parents of our school to our monthly PTA Meeting.

The copy should include:

PTA Meeting
This Wednesday
8:40am
in the Multi Purpose Room

All Welcome!

```html
<!DOCTYPE html>
<html lang="en">
<head>
<meta charset="UTF-8">
<title>PTA Meeting Poster</title>
<link rel="stylesheet" href="https://fonts.googleapis.com/css2?family=Fredoka:wdth,wght@75..125,300..700&family=Nunito:wght@500&display=swap">
<style>
  :root {
    --paper: #ffffff;
    --ink: #0a0a0a;
    --school-red: #e8161b;
    --flag-red: #c8202c;
    --flag-blue: #2b2f6b;
    --flag-white: #f2f0ee;
  }
  html, body {
    margin: 0;
    padding: 0;
    overflow: hidden;
    background: var(--paper);
  }
  .poster {
    position: relative;
    width: 848px;
    height: 1200px;
    background: var(--paper);
    overflow: hidden;
    font-family: "Fredoka", "Arial Rounded MT Bold", sans-serif;
    color: var(--ink);
  }
  .school-mark {
    position: absolute;
    left: 38px;
    top: 18px;
    width: 144px;
    height: 144px;
    border-radius: 50%;
    border: 4px solid var(--ink);
    box-sizing: border-box;
    background: var(--paper);
  }
  .school-name {
    position: absolute;
    left: 231px;
    top: 44px;
    margin: 0;
    font-family: "Nunito", "Tahoma", sans-serif;
    font-weight: 500;
    font-size: 48px;
    line-height: 1;
    color: var(--school-red);
    white-space: nowrap;
  }
  .shield {
    position: absolute;
    left: 173px;
    top: 217px;
    width: 482px;
    height: 476px;
  }
  .shield-title {
    margin: 0;
    font-weight: 700;
    font-stretch: 125%;
  }
  .shield-title span {
    position: absolute;
    left: 173px;
    width: 482px;
    text-align: center;
    line-height: 1;
    white-space: nowrap;
  }
  .shield-title .pta {
    top: 392px;
    font-size: 98px;
    letter-spacing: 6px;
  }
  .shield-title .meeting {
    top: 500px;
    font-size: 80px;
    letter-spacing: 1px;
  }
  .details {
    position: absolute;
    left: 0;
    top: 706px;
    width: 848px;
    margin: 0;
    text-align: center;
    font-weight: 700;
    font-stretch: 86%;
    font-size: 86px;
    line-height: 90px;
  }
  .details span { display: block; white-space: nowrap; }
  .welcome {
    position: absolute;
    left: 0;
    top: 1058px;
    width: 848px;
    margin: 0;
    text-align: center;
    font-weight: 700;
    font-stretch: 92%;
    font-size: 68px;
    line-height: 1;
    white-space: nowrap;
  }
</style>
</head>
<body>
  <main class="poster">
    <header>
      <div class="school-mark" aria-hidden="true"></div>
      <p class="school-name">Kestrel Vale High</p>
    </header>

    <svg class="shield" viewBox="0 0 482 443" preserveAspectRatio="none">
      <defs>
        <clipPath id="shield-clip">
          <path d="M18,18 Q130,32 241,4 Q352,32 464,18 L477,70 Q463,112 471,160 Q490,300 372,360 Q282,392 241,438 Q200,392 110,360 Q-8,300 11,160 Q19,112 5,70 Z"/>
        </clipPath>
        <linearGradient id="flag-tones" x1="0" y1="0" x2="1" y2="0.4">
          <stop offset="0" stop-color="var(--flag-blue)"/>
          <stop offset="0.42" stop-color="var(--flag-blue)"/>
          <stop offset="0.55" stop-color="var(--flag-white)"/>
          <stop offset="0.75" stop-color="var(--flag-red)"/>
          <stop offset="1" stop-color="var(--flag-red)"/>
        </linearGradient>
      </defs>
      <g clip-path="url(#shield-clip)">
        <rect width="482" height="443" fill="var(--paper)"/>
        <rect class="shield-flag" width="482" height="142" fill="url(#flag-tones)" role="img" aria-label="Waving American flag"/>
        <rect y="138" width="482" height="9" fill="var(--ink)"/>
      </g>
      <path d="M18,18 Q130,32 241,4 Q352,32 464,18 L477,70 Q463,112 471,160 Q490,300 372,360 Q282,392 241,438 Q200,392 110,360 Q-8,300 11,160 Q19,112 5,70 Z" fill="none" stroke="var(--ink)" stroke-width="9" stroke-linejoin="round"/>
    </svg>

    <h1 class="shield-title">
      <span class="pta">PTA</span>
      <span class="meeting">MEETING</span>
    </h1>

    <p class="details">
      <span>Join Us Wednesday</span>
      <span>8.40am in the</span>
      <span>Multi Purpose Room</span>
    </p>

    <p class="welcome">Everyone Welcome</p>
  </main>
</body>
</html>
```